Detox Poster Design Project

I am a naturopath that works in Melbourne. I require a poster that I can put up in my natural therapies clinic that is advertising a detox program that I am offering. The program runs for 3 or 6 weeks and is designed to help your liver, gut and kidney cleanse toxins more efficiently, leaving you feeling energised and healthy.

I would like to see designs that are fresh, organic, clear and contemporary to look at. I want to sell the idea of feeling good, wellbeing and vitality to the potential client. Colours I like include greens, greys and blues.

The final design should communicate health and happiness.

• Please include the photo of the woman in nature.Poster size will be A2 594mm by 420mm
• I have attached the design work for my business cards that you can use. It would be great if the colours and style are in keeping with the existing design work for my business. I have also attached an extra image (almond milk photo) just in case you could see a use for it.

Many thanks.
• No hippy, new age looking design.

```html
<!DOCTYPE html>
<html lang="en">
<head>
<meta charset="utf-8">
<title>Sensible Detox</title>
<link rel="stylesheet" href="https://fonts.googleapis.com/css2?family=Quicksand:wght@300;400;500&display=swap">
<style>
  :root {
    --leaf-deep: #2f5a2f;
    --band-green: rgba(70, 155, 92, 0.62);
    --panel-green: #b8ddb3;
    --accent-blue: #2aa7d5;
    --white: #ffffff;
    --photo-light: #f3f6ee;
    --photo-lime: #a9d46a;
    --photo-mid: #6fa650;
    --photo-dark: #2f5a2a;
    --photo-grey: #a3a69e;
  }
  html, body {
    margin: 0;
    padding: 0;
    overflow: hidden;
    background: #ffffff;
  }
  .poster {
    position: relative;
    width: 849px;
    height: 1200px;
    overflow: hidden;
    font-family: "Quicksand", sans-serif;
  }
  .hero-photo {
    position: absolute;
    inset: 0;
    background:
      radial-gradient(ellipse 260px 240px at 760px 110px, rgba(255,255,255,0.97) 0%, rgba(255,255,255,0) 100%),
      radial-gradient(ellipse 240px 260px at 60px 140px, rgba(236,238,232,0.95) 0%, rgba(236,238,232,0) 100%),
      radial-gradient(ellipse 200px 160px at 640px 320px, rgba(190,225,120,0.85) 0%, rgba(190,225,120,0) 100%),
      radial-gradient(ellipse 220px 200px at 760px 700px, rgba(170,215,80,0.8) 0%, rgba(170,215,80,0) 100%),
      radial-gradient(ellipse 260px 220px at 300px 260px, rgba(60,110,50,0.75) 0%, rgba(60,110,50,0) 100%),
      radial-gradient(ellipse 300px 220px at 430px 700px, rgba(120,150,80,0.7) 0%, rgba(120,150,80,0) 100%),
      radial-gradient(ellipse 260px 260px at 150px 700px, rgba(150,170,120,0.7) 0%, rgba(150,170,120,0) 100%),
      linear-gradient(165deg, var(--photo-light) 0%, var(--photo-mid) 35%, var(--photo-dark) 62%, var(--photo-mid) 78%, var(--photo-grey) 100%);
  }
  .decor {
    position: absolute;
    inset: 0;
  }
  .title-band {
    position: absolute;
    left: 0;
    top: 372px;
    width: 849px;
    height: 190px;
    background: var(--band-green);
    color: var(--white);
    text-align: center;
  }
  .title {
    margin: 0;
    padding-top: 16px;
    font-weight: 300;
    font-size: 110px;
    line-height: 1;
    letter-spacing: 0.5px;
  }
  .tagline {
    margin: 14px 0 0;
    font-weight: 400;
    font-size: 40px;
    line-height: 1;
  }
  .message {
    position: absolute;
    left: 27px;
    top: 878px;
    margin: 0;
    color: var(--leaf-deep);
    font-weight: 500;
    font-size: 34px;
    line-height: 49px;
  }
  .message .highlight {
    color: var(--accent-blue);
  }
  .brand {
    position: absolute;
    left: 24px;
    top: 1122px;
    display: flex;
    align-items: center;
    gap: 10px;
    color: var(--accent-blue);
    font-weight: 400;
    font-size: 22px;
    line-height: 24px;
  }
  .brand-dot {
    width: 40px;
    height: 40px;
    border-radius: 50%;
    background: var(--accent-blue);
  }
  .contact {
    position: absolute;
    left: 260px;
    top: 1111px;
    color: var(--leaf-deep);
    font-weight: 500;
    font-size: 26px;
    line-height: 37px;
  }
  .contact .label {
    display: inline-block;
    width: 70px;
  }
</style>
</head>
<body>
<main class="poster">
  <div class="hero-photo" role="img" aria-label="Photo of a woman seen from behind with arms raised, standing in lush sunlit green rainforest"></div>

  <svg class="decor" width="849" height="1200" viewBox="0 0 849 1200" aria-hidden="true">
    <polygon points="0,0 560,0 0,330" fill="rgba(225,228,220,0.35)"/>
    <polygon points="0,330 560,0 640,0 0,370" fill="rgba(120,190,120,0.35)"/>
    <polygon points="0,250 430,0 470,0 0,275" fill="rgba(255,255,255,0.25)"/>
    <polygon points="0,640 849,1040 849,1200 0,1200" fill="rgba(160,163,155,0.55)"/>
    <polygon points="0,585 849,980 849,1040 0,640" fill="rgba(150,200,150,0.35)"/>
    <path d="M0,845 Q230,760 560,880 Q770,965 835,1200 L0,1200 Z" fill="var(--panel-green)"/>
  </svg>

  <section class="title-band">
    <h1 class="title">Sensible Detox.</h1>
    <p class="tagline">Your path to a healthier, re-energized you</p>
  </section>

  <p class="message">
    Overindulge<br>
    over the holidays? Press<br>
    reset on your bad eating habits<br>
    and start feeling <span class="highlight">energized &amp; vital</span>.
  </p>

  <div class="brand">
    <span class="brand-dot"></span>
    <span>Clara Wendell<br>Naturopath</span>
  </div>

  <div class="contact">
    <div><span class="label">Call</span>| 0400 318 264</div>
    <div><span class="label">Email</span>| hello@greenleafnaturopath.com</div>
  </div>
</main>
</body>
</html>
```